business cards, stationary, envelopes,
Brindle Houses business cards
business cards, stationary, envelopes,  - Construction
Creative Brief
Professional
Dale R. Morrow
President
412 NE State Route 19 #208 Blue Springs, MO 64015
dale@brindlehousesmk.example
www.brindlehousesmk.example

```html
<!DOCTYPE html>
<html lang="en">
<head>
<meta charset="utf-8">
<title>Brindle Houses – Business Cards</title>
<link href="https://fonts.googleapis.com/css2?family=Arimo:wght@400;700&display=swap" rel="stylesheet">
<style>
  :root {
    --bg: #e9e6e1;
    --card: #1c1c1e;
    --card-edge: #2a2a2c;
    --gold: #d9a63a;
    --gold-light: #f3d27a;
    --gold-dark: #a9771c;
    --red: #c8191f;
    --text-light: #e6e6e6;
  }
  * { box-sizing: border-box; margin: 0; padding: 0; }
  html, body { width: 1200px; height: 852px; overflow: hidden; }
  body {
    background: var(--bg);
    font-family: "Arimo", Arial, sans-serif;
    position: relative;
  }
  .card {
    position: absolute;
    width: 540px;
    height: 310px;
    border-radius: 18px;
    background: radial-gradient(ellipse at 40% 30%, var(--card-edge), var(--card) 70%);
    overflow: hidden;
    box-shadow: 0 6px 18px rgba(0,0,0,.25);
  }
  .card--front { left: 40px; top: 271px; }
  .card--back { left: 620px; top: 271px; }
  .card__band {
    position: absolute; left: 0; right: 0; bottom: 0; height: 28px;
    background: linear-gradient(180deg, var(--gold-light), var(--gold) 45%, var(--gold-dark));
  }
  .card__band::before {
    content: ""; position: absolute; left: 0; right: 0; top: -7px; height: 7px;
    background: var(--red);
  }
  .brand {
    position: absolute;
    display: flex; align-items: center; gap: 10px;
    color: var(--gold);
    font-weight: 700;
    font-size: 32px;
    letter-spacing: .5px;
    white-space: nowrap;
  }
  .brand__mark { width: 14px; height: 14px; background: var(--red); flex: none; }
  .person__name { color: var(--gold); font-weight: 700; font-size: 15px; }
  .person__title { color: var(--gold); font-size: 11px; margin-top: 3px; }
  .address { color: var(--text-light); font-size: 12px; line-height: 1.45; white-space: nowrap; }
  .contacts { list-style: none; color: var(--text-light); font-size: 12px; }
  .contacts li { display: flex; align-items: center; gap: 7px; height: 20px; white-space: nowrap; }
  .contacts svg { width: 12px; height: 12px; flex: none; }
  .divider { position: absolute; width: 1px; background: linear-gradient(var(--card), #8a8a8a, var(--card)); }

  /* front */
  .card--front .brand { left: 100px; top: 78px; }
  .card--front .person { position: absolute; left: 80px; top: 146px; }
  .card--front .address { position: absolute; left: 40px; top: 200px; }
  .card--front .divider { left: 292px; top: 130px; height: 130px; }
  .card--front .contacts { position: absolute; left: 306px; top: 130px; }

  /* back */
  .card--back .person { position: absolute; left: 300px; top: 34px; }
  .card--back .address { position: absolute; left: 300px; top: 84px; }
  .card--back .divider { left: 286px; top: 30px; height: 230px; }
  .card--back .contacts { position: absolute; left: 300px; top: 140px; }
  .card--back .brand { left: 26px; top: 190px; font-size: 26px; gap: 8px; }
  .card--back .brand__mark { width: 12px; height: 12px; }
</style>
</head>
<body>
  <svg width="0" height="0" style="position:absolute">
    <defs>
      <symbol id="icon-phone" viewBox="0 0 12 12"><path d="M2.5 1h2l1 2.5-1.3.9a6 6 0 0 0 3.4 3.4l.9-1.3 2.5 1v2a1 1 0 0 1-1 1A9 9 0 0 1 1.5 2a1 1 0 0 1 1-1z" fill="#d9a63a"/></symbol>
      <symbol id="icon-mobile" viewBox="0 0 12 12"><rect x="3" y="0.5" width="6" height="11" rx="1.2" fill="#d9a63a"/><rect x="4" y="2" width="4" height="7" fill="#1c1c1e"/></symbol>
      <symbol id="icon-fax" viewBox="0 0 12 12"><rect x="1" y="4" width="10" height="6" rx="1" fill="#d9a63a"/><rect x="3" y="1" width="6" height="3" fill="#d9a63a"/><rect x="3" y="8" width="6" height="3" fill="#f3d27a"/></symbol>
      <symbol id="icon-mail" viewBox="0 0 12 12"><circle cx="6" cy="6" r="6" fill="#d9a63a"/><rect x="2.8" y="3.8" width="6.4" height="4.4" fill="#1c1c1e"/><path d="M2.8 3.8 6 6.4 9.2 3.8" stroke="#d9a63a" stroke-width=".8" fill="none"/></symbol>
      <symbol id="icon-web" viewBox="0 0 12 12"><circle cx="6" cy="6" r="6" fill="#d9a63a"/><circle cx="6" cy="6" r="3.5" fill="none" stroke="#1c1c1e" stroke-width=".9"/><path d="M2.5 6h7M6 2.5c-1.5 2-1.5 5 0 7M6 2.5c1.5 2 1.5 5 0 7" stroke="#1c1c1e" stroke-width=".8" fill="none"/></symbol>
    </defs>
  </svg>

  <section class="card card--front">
    <div class="brand"><span class="brand__mark"></span>Brindle Houses</div>
    <div class="person">
      <p class="person__name">Dale R. Morrow</p>
      <p class="person__title">President</p>
    </div>
    <p class="address">412 NE State Route 19 #208<br>Cedar Hollow, KS 66951</p>
    <span class="divider"></span>
    <ul class="contacts">
      <li><svg><use href="#icon-phone"/></svg>816-555-0142</li>
      <li><svg><use href="#icon-mobile"/></svg>816-555-0187</li>
      <li><svg><use href="#icon-fax"/></svg>816-555-0163</li>
      <li><svg><use href="#icon-mail"/></svg>dale@brindlehousesmk.example</li>
      <li><svg><use href="#icon-web"/></svg>www.brindlehousesmk.example</li>
    </ul>
    <div class="card__band"></div>
  </section>

  <section class="card card--back">
    <div class="person">
      <p class="person__name">Dale R. Morrow</p>
      <p class="person__title">President</p>
    </div>
    <p class="address">412 NE State Route 19 #208<br>Cedar Hollow, KS 66951</p>
    <span class="divider"></span>
    <ul class="contacts">
      <li><svg><use href="#icon-phone"/></svg>816-555-0142</li>
      <li><svg><use href="#icon-mobile"/></svg>816-555-0187</li>
      <li><svg><use href="#icon-fax"/></svg>816-555-0163</li>
      <li><svg><use href="#icon-mail"/></svg>dale@brindlehousesmk.example</li>
      <li><svg><use href="#icon-web"/></svg>www.brindlehousesmk.example</li>
    </ul>
    <div class="brand"><span class="brand__mark"></span>Brindle Houses</div>
    <div class="card__band"></div>
  </section>
</body>
</html>
```